Cultural Values, and Purpose, Vision and Mission statements design

We have recently created Cultural Values, and Purpose, Vision and Mission statements for a client’s business. We would like a visual representation created of each of these, to be hung on display in their office. For this project, we would like four (4) graphic design prints drawn up that depict:1. Purpose2. Vision3. Mission4. Cultural ValuesAll print designs should use a recurring, common theme, and be reflective of the business’ colours (see attached logo.)Please read and follow specifications in attached design brief.
Updates

Need extra days to review

Target Market(s)

Females, aged between 37 and 57 years old, who are family orientated, living locally, married and have between 1 and 3 children living at home.

Requirements
Must have
• Photoshop (PSD) format: All completed design will need to be in Photoshop (PSD) format before being handed over. This is to ensure that we can make alterations before printing if necessary.
• Quality: All designs must be 300 pixels resolution or higher.
• Purpose, Vision & Mission Designs Dimensions: The dimensions for each of the Purpose, Vision and Mission designs will need to be 30.5cm x 40.6cm (portrait, rectangle shape) with a surrounding 3.8cm border as it will be printed onto canvas matching these specifications.
• Cultural Values Dimensions: There are no specific dimensions required for the Cultural Values so the designer should feel free to display them best they see fit.
• Theme: All must follow the same theme and be reflective of the business's colours and logo.

```html
<!DOCTYPE html>
<html lang="en">
<head>
<meta charset="utf-8">
<title>KestrelAuto — Mission</title>
<link rel="stylesheet" href="https://fonts.googleapis.com/css2?family=Carlito:wght@700&family=Saira+Stencil+One&display=swap">
<style>
  :root {
    --orange: #f1801f;
    --grey-dark: #737373;
    --grey-rule: #9a9a9a;
    --ink: #333333;
    --paper: #ffffff;
    --faint: #ebebec;
  }
  * { margin: 0; padding: 0; box-sizing: border-box; }
  html, body { width: 902px; height: 1200px; overflow: hidden; background: var(--paper); }
  .poster { position: relative; width: 902px; height: 1200px; overflow: hidden; background: var(--paper); }
  .decor-rocket {
    position: absolute; left: 70px; top: 205px; width: 770px; height: 760px;
    border-radius: 50%;
    background: radial-gradient(circle at 55% 45%, rgba(235,235,236,0.55) 0%, rgba(235,235,236,0.25) 55%, rgba(235,235,236,0) 72%);
  }
  .brand-plate {
    position: absolute; left: 132px; top: 66px; width: 632px; height: 148px;
    background: var(--paper); border: 1px solid #e2e2e2;
    box-shadow: 0 14px 14px -10px rgba(0,0,0,0.18);
    display: flex; align-items: center; justify-content: center;
  }
  .brand-name {
    font-family: "Carlito", "Lato", sans-serif; font-weight: 700;
    font-size: 78px; color: var(--orange); letter-spacing: 1px;
  }
  .title {
    position: absolute; left: 0; width: 902px; top: 240px;
    text-align: center;
    font-family: "Saira Stencil One", "Saira", sans-serif;
    font-size: 196px; line-height: 1; color: var(--orange);
    font-style: italic;
  }
  .rule { position: absolute; left: 96px; top: 471px; width: 703px; height: 2px; background: var(--grey-rule); }
  .statement {
    position: absolute; left: 60px; width: 782px; top: 486px;
    text-align: center;
    font-family: "Carlito", "Lato", sans-serif; font-weight: 700;
    font-size: 37px; line-height: 49px; color: var(--ink);
  }
  .bands { position: absolute; left: 0; top: 0; width: 902px; height: 1200px; }
</style>
</head>
<body>
  <main class="poster">
    <div class="decor-rocket" role="img" aria-label="Faint outline illustration of a rocket launching"></div>

    <header class="brand-plate">
      <span class="brand-name">KestrelAuto</span>
    </header>

    <h1 class="title">Mission</h1>
    <div class="rule"></div>
    <p class="statement">Through the delivery of highquality automotive specialists through out the Latrobe Valley benefits.</p>

    <svg class="bands" viewBox="0 0 1127 1500" preserveAspectRatio="none" aria-hidden="true">
      <polygon points="0,1180 640,1060 683,1083 0,1213" fill="var(--orange)"/>
      <polygon points="0,1225 1127,1013 1127,1052 0,1267" fill="var(--orange)"/>
      <polygon points="0,1266 1127,1051 1127,1500 0,1500" fill="var(--grey-dark)"/>
      <polygon points="727,1140 1127,1063 1127,1095 765,1163" fill="var(--orange)"/>
    </svg>
  </main>
</body>
</html>
```